private relaxation massage therapist business card

I want a card that does not give a physical address as I am able to massage at home as well as be mobile. I want on the back somewhere to put appointment details and also my bank acct details for payment being to acct 38 7402 0061948 00
I have a Certificate in Relaxation Massage from KPTA 2014
I would like to use blue colours and maybe have some fluffy clouds somewhere on the business card.

Industry/Entity Type

Massage

Contact Information for Business Card

Fiona Marsh
Relaxation Massage Therapist

telephone 0216 842 197 or 09 4718335
email fionamarsh72@quellbox.com

Requirements
Must have
• bold lettering, lots of white space, On the reverse of the card some lines in a box for me to write appointment times also on reverse my bank acct details for payment on line.

```html
<!DOCTYPE html>
<html lang="en">
<head>
<meta charset="utf-8">
<title>Fiona Marsh – Relaxation Massage Therapist – Business Card</title>
<link href="https://fonts.googleapis.com/css2?family=Open+Sans:wght@300;400;600;700&display=swap" rel="stylesheet">
<style>
  :root {
    --page-bg: #ececec;
    --card-bg: #ffffff;
    --brand-blue: #2f73a8;
    --brand-dark: #1f2a33;
    --text-grey: #6b6f73;
    --text-dark: #222629;
    --rule-grey: #9a9ea2;
    --cloud-light: #e6eef4;
    --cloud-mid: #cfdde8;
  }
  * { box-sizing: border-box; margin: 0; padding: 0; }
  html, body {
    width: 1200px; height: 800px; overflow: hidden;
    background: var(--page-bg);
    font-family: "Open Sans", Arial, sans-serif;
  }
  .sheet {
    width: 1200px; height: 800px;
    display: flex; align-items: center; justify-content: center; gap: 40px;
  }
  .card {
    position: relative;
    width: 540px; height: 330px;
    background: var(--card-bg);
    border-radius: 16px;
    box-shadow: 0 6px 18px rgba(0,0,0,0.12);
    overflow: hidden;
  }

  /* ---------- Front ---------- */
  .brand-name {
    font-weight: 700;
    font-size: 46px;
    line-height: 1;
    color: var(--brand-blue);
    letter-spacing: 0.5px;
  }
  .brand-title {
    font-weight: 300;
    font-size: 15px;
    letter-spacing: 0.6px;
    color: var(--text-grey);
    text-transform: uppercase;
    margin-top: 8px;
  }
  .front .brand { position: absolute; left: 40px; top: 62px; }
  .front .divider {
    position: absolute; left: 300px; top: 160px;
    width: 1px; height: 80px; background: var(--rule-grey);
  }
  .contact-list {
    position: absolute; left: 316px; top: 166px;
    list-style: none;
  }
  .contact-list li {
    display: flex; align-items: center; gap: 8px;
    font-size: 15px; font-weight: 600; color: var(--text-dark);
    line-height: 1.55;
  }
  .contact-list li.email { font-size: 14px; }
  .contact-icon { width: 13px; height: 13px; flex: none; }

  /* ---------- Back ---------- */
  .back .brand { position: absolute; left: 32px; top: 28px; }
  .back .brand-name { color: var(--brand-dark); font-size: 34px; }
  .back .brand-title { font-size: 12px; color: var(--text-dark); margin-top: 6px; }
  .clouds {
    position: absolute; left: 0; bottom: 0;
    width: 330px; height: 170px;
    background: linear-gradient(160deg, var(--cloud-light) 0%, var(--cloud-mid) 100%);
    border-top-right-radius: 140px 120px;
  }
  .appointment {
    position: absolute; right: 34px; top: 36px; width: 200px;
  }
  .appointment-heading {
    font-size: 17px; font-weight: 400; color: var(--text-dark);
    margin-bottom: 18px;
  }
  .field {
    display: flex; align-items: flex-end; gap: 6px;
    font-size: 13px; color: var(--text-grey);
    margin-bottom: 18px;
  }
  .field .line {
    flex: 1; border-bottom: 1px dotted var(--rule-grey); height: 14px;
  }
  .account {
    position: absolute; right: 34px; bottom: 34px;
    font-size: 13px; color: var(--text-dark); letter-spacing: 0.3px;
  }
</style>
</head>
<body>
<main class="sheet">

  <section class="card back" aria-label="Card back">
    <div class="clouds" role="img" aria-label="Soft pale blue fluffy clouds"></div>
    <div class="brand">
      <div class="brand-name">Fiona Marsh</div>
      <div class="brand-title">Relaxation Massage Therapist</div>
    </div>
    <div class="appointment">
      <h2 class="appointment-heading">Appointment</h2>
      <div class="field"><span>Date:</span><span class="line"></span></div>
      <div class="field"><span>Time:</span><span class="line"></span></div>
    </div>
    <div class="account">ACCT: 38 7402 0061948 00</div>
  </section>

  <section class="card front" aria-label="Card front">
    <div class="brand">
      <div class="brand-name">Fiona Marsh</div>
      <div class="brand-title">Relaxation Massage Therapist</div>
    </div>
    <div class="divider"></div>
    <ul class="contact-list">
      <li>
        <svg class="contact-icon" viewBox="0 0 13 13" aria-hidden="true">
          <rect width="13" height="13" rx="2" fill="#2f73a8"/>
          <rect x="4" y="2.5" width="5" height="8" rx="1" fill="none" stroke="#fff" stroke-width="1.2"/>
        </svg>
        0216 842 197
      </li>
      <li>
        <svg class="contact-icon" viewBox="0 0 13 13" aria-hidden="true">
          <rect width="13" height="13" rx="2" fill="#2f73a8"/>
          <path d="M4 3 L5.6 3 L6.2 5 L5.2 5.8 Q6 7.4 7.4 8 L8.2 7 L10 7.6 L10 9.2 Q6.5 9.6 4.2 7 Q3.2 5.5 4 3Z" fill="#fff"/>
        </svg>
        09 4718335
      </li>
      <li class="email">
        <svg class="contact-icon" viewBox="0 0 13 13" aria-hidden="true">
          <rect width="13" height="13" rx="2" fill="#2f73a8"/>
          <rect x="2.5" y="3.5" width="8" height="6" fill="none" stroke="#fff" stroke-width="1.1"/>
          <path d="M2.5 3.5 L6.5 7 L10.5 3.5" fill="none" stroke="#fff" stroke-width="1.1"/>
        </svg>
        fionamarsh72@quellbox.com
      </li>
    </ul>
  </section>

</main>
</body>
</html>
```